One-Page Flat Design for SEO Company [2 DAYS]

We need a one-page flat design for our SEO company. Our current website is http://www.rankloft.com/. We are looking to completely re-design the site using new flat design techniques.
Below are some examples of the type of style we're going after:
http://quormel.com/
http://tobyrand.co.uk/
https://pentaly.co/
http://milesporter.me/
As you can see- flat, clean, minimal. It is very important you follow this type of style.
For colour scheme, you may use one of the pre-made colour palettes from here:
http://www.vornacle.com/blog/inspiration/24-flat-designs-with-compelling-color-palettes
I've attached a wireframe to be followed.
Hi,

```html
<!DOCTYPE html>
<html lang="en">
<head>
<meta charset="utf-8">
<title>RankLoft – SEO Services</title>
<link href="https://fonts.googleapis.com/css2?family=Open+Sans:wght@400;600;700&family=PT+Sans+Narrow:wght@400;700&display=swap" rel="stylesheet">
<style>
:root{
  --header:#2f2b29;
  --orange:#f5834c;
  --teal:#40c1a9;
  --sky:#80bbc5;
  --slate:#4a4b5c;
  --navy:#30506f;
  --contact:#fd8349;
  --footer:#2b2b2e;
  --red:#e9505b;
  --white:#ffffff;
  --card-grey:#ebebeb;
}
*{box-sizing:border-box;margin:0;padding:0}
html,body{width:1200px;height:3180px;overflow:hidden}
body{font-family:"Open Sans",Arial,sans-serif;color:var(--white);background:var(--white)}
section,header,footer{position:relative;width:1200px;overflow:hidden}
.abs{position:absolute}
.center{left:0;width:1200px;text-align:center}

/* header */
.site-header{height:83px;background:var(--header)}
.brand{left:46px;top:18px;display:flex;align-items:center;gap:8px}
.brand-mark{width:16px;height:16px;background:var(--orange)}
.brand-name{font-weight:700;font-size:27px;color:var(--orange);line-height:1}
.brand-tag{left:70px;top:52px;font-size:9px;color:#d8d8d8;letter-spacing:.5px}
.main-nav{right:26px;top:24px;display:flex}
.main-nav a{display:block;padding:9px 18px;margin-left:10px;font-size:15px;color:var(--white);text-decoration:none;text-transform:uppercase}
.main-nav a.active{background:var(--orange)}

/* hero */
.hero{height:437px;background:var(--white)}
.hero-devices{left:660px;top:50px;width:480px;height:320px;border-radius:8px;background:linear-gradient(160deg,#f1f1f1,#cfd0d2 60%,#e6e6e6)}
.hero-title{left:42px;top:70px;z-index:2;font-size:40px;font-weight:600;line-height:56px;color:var(--orange)}
.hero-sub{left:42px;top:202px;z-index:2;font-size:19px;line-height:30px;color:#555}
.hero-dots{left:44px;top:290px;display:flex;gap:5px}
.hero-dots span{width:12px;height:12px;border-radius:50%;background:#b8bcc6}
.hero-dots span:first-child{background:#3c4a63}

/* why */
.why{height:434px;background:var(--teal)}
.section-title{font-size:36px;font-weight:400;text-transform:uppercase;letter-spacing:.5px}
.why .section-title{top:50px}
.feature{top:137px;width:240px;text-align:center}
.feature-art{display:block;margin:0 auto;width:172px;height:172px;border-radius:50%;border:5px solid var(--white);background:radial-gradient(circle at 50% 45%,#e4e4e4,#b9b9b9)}
.feature-label{margin-top:22px;font-size:18px;font-weight:700;text-transform:uppercase;letter-spacing:.5px}
.arrow{width:40px;height:70px}

/* plans */
.plans{height:694px;background:var(--sky)}
.plans .section-title{top:44px}
.plans-sub{top:110px;font-size:13px}
.plan{top:176px;width:229px;height:445px;background:var(--white);border-radius:4px;text-align:center;color:#333;box-shadow:0 1px 3px rgba(0,0,0,.12)}
.plan-name{height:76px;line-height:76px;font-size:15px;font-weight:700;text-transform:uppercase}
.plan-price{height:45px;line-height:45px;background:var(--card-grey);font-family:"PT Sans Narrow",Arial,sans-serif;font-size:21px}
.plan-features{list-style:none;margin-top:18px;font-size:12px;color:#999;line-height:30px}
.plan-features b{color:#888}
.plan-btn{display:inline-block;margin-top:24px;width:164px;height:45px;line-height:45px;font-size:14px;font-weight:700;text-transform:uppercase;color:var(--white);background:var(--sky);border-bottom:3px solid #5f9aa4;letter-spacing:.5px}
.plan.featured{top:165px;height:465px}
.plan.featured .plan-name{height:58px;line-height:58px;background:var(--orange);color:var(--white);border-radius:4px 4px 0 0;font-size:14px}
.plan.featured .plan-price{background:#f7a174;color:var(--white)}
.plan.featured .plan-btn{background:var(--orange);border-bottom-color:#d2622e}

/* cta */
.cta{height:140px;background:var(--slate)}
.cta-devices{left:64px;top:22px;width:154px;height:100px;border-radius:4px;background:linear-gradient(160deg,#e8e8e8,#a6a7ab)}
.cta-text{left:254px;top:56px;font-size:18px;white-space:nowrap}
.cta-btn{left:927px;top:45px;width:150px;height:48px;line-height:48px;text-align:center;background:var(--red);font-size:19px;font-weight:600;text-transform:uppercase}

/* services */
.services{height:528px;background:var(--navy)}
.services .section-title{top:40px}
.services-sub{top:104px;font-size:13px;line-height:22px}
.service{top:190px;width:280px;text-align:center}
.service-icon{display:block;margin:0 auto;width:172px;height:172px}
.service-label{margin-top:20px;font-size:18px;font-weight:700;text-transform:uppercase}
.service-text{margin-top:14px;font-size:13px;line-height:21px}

/* contact */
.contact{height:519px;background:var(--contact)}
.contact .section-title{top:28px}
.field{background:var(--white);border:2px solid #cfcfcf;color:#666;font-size:11px;padding:12px 10px}
.contact-btn{left:526px;top:370px;width:148px;height:49px;line-height:49px;text-align:center;background:#3d3d3d;font-size:18px;text-transform:uppercase}
.social-links{top:470px;display:flex;justify-content:center;gap:48px;font-size:20px;text-transform:uppercase}

/* footer */
.site-footer{height:345px;background:var(--footer)}
.footer-brand{top:40px;display:flex;justify-content:center;align-items:center;gap:8px}
.footer-tag{top:80px;font-size:9px;color:#d8d8d8;letter-spacing:.5px}
.footer-text{top:108px;font-size:13px;line-height:24px}
.footer-social{top:194px;display:flex;justify-content:center;gap:8px}
.footer-social span{width:42px;height:42px;border-radius:50%;background:var(--white)}
.copyright{top:270px;font-size:13px}
</style>
</head>
<body>

<header class="site-header">
  <div class="abs brand"><span class="brand-mark"></span><span class="brand-name">RankLoft</span></div>
  <div class="abs brand-tag">LET US BOOST YOUR RANKINGS</div>
  <nav class="abs main-nav">
    <a class="active">Home</a><a>About</a><a>Work</a><a>Services</a><a>Team</a><a>Contact</a>
  </nav>
</header>

<section class="hero">
  <div class="abs hero-devices" role="img" aria-label="Desktop monitor, laptop, tablet and phone showing the site"></div>
  <h1 class="abs hero-title">Finally, SEO service that<br>actually work.</h1>
  <p class="abs hero-sub">Top-notch services that are guaranteed to boost your<br>search engine rankings. 100% Searchly friendly.</p>
  <div class="abs hero-dots"><span></span><span></span><span></span><span></span></div>
</section>

<section class="why">
  <h2 class="abs center section-title">Why choose RankLoft</h2>
  <svg class="abs arrow" style="left:92px;top:188px" viewBox="0 0 40 70"><polyline points="34,2 4,35 34,68" fill="none" stroke="#2a7d6d" stroke-width="2.5"/></svg>
  <svg class="abs arrow" style="left:1066px;top:188px" viewBox="0 0 40 70"><polyline points="6,2 36,35 6,68" fill="none" stroke="#2a7d6d" stroke-width="2.5"/></svg>
  <div class="abs feature" style="left:200px"><span class="feature-art" role="img" aria-label="Branding illustration with stationery and brand guides"></span><div class="feature-label">Branding</div></div>
  <div class="abs feature" style="left:480px"><span class="feature-art" role="img" aria-label="Design illustration with screen and devices"></span><div class="feature-label">Design</div></div>
  <div class="abs feature" style="left:762px"><span class="feature-art" role="img" aria-label="Development illustration with screen and shapes"></span><div class="feature-label">Development</div></div>
</section>

<section class="plans">
  <h2 class="abs center section-title">Select a booster plan</h2>
  <p class="abs center plans-sub">Our company prides itself in keeping the prices low for whatever it takes.</p>

  <div class="abs plan" style="left:153px">
    <div class="plan-name">Professional</div><div class="plan-price">$50/Month</div>
    <ul class="plan-features"><li><b>2x</b> option 1</li><li><b>Free</b> option 2</li><li><b>Unlimited</b> option 3</li><li><b>Unlimited</b> option 4</li><li><b>1x</b> option 5</li><li><b>10GB</b> amount of space</li><li><b>10</b> Email account</li></ul>
    <span class="plan-btn">Get started</span>
  </div>
  <div class="abs plan" style="left:383px">
    <div class="plan-name">Professional</div><div class="plan-price">$50/Month</div>
    <ul class="plan-features"><li><b>2x</b> option 1</li><li><b>Free</b> option 2</li><li><b>Unlimited</b> option 3</li><li><b>Unlimited</b> option 4</li><li><b>1x</b> option 5</li><li><b>10GB</b> amount of space</li><li><b>10</b> Email account</li></ul>
    <span class="plan-btn">Get started</span>
  </div>
  <div class="abs plan featured" style="left:614px">
    <div class="plan-name">Professional</div><div class="plan-price">$50/Month</div>
    <ul class="plan-features"><li><b>2x</b> option 1</li><li><b>Free</b> option 2</li><li><b>Unlimited</b> option 3</li><li><b>Unlimited</b> option 4</li><li><b>1x</b> option 5</li><li><b>10GB</b> amount of space</li><li><b>10</b> Email account</li></ul>
    <span class="plan-btn">Purchase now</span>
  </div>
  <div class="abs plan" style="left:844px">
    <div class="plan-name">Professional</div><div class="plan-price">$50/Month</div>
    <ul class="plan-features"><li><b>2x</b> option 1</li><li><b>Free</b> option 2</li><li><b>Unlimited</b> option 3</li><li><b>Unlimited</b> option 4</li><li><b>1x</b> option 5</li><li><b>10GB</b> amount of space</li><li><b>10</b> Email account</li></ul>
    <span class="plan-btn">Get started</span>
  </div>
</section>

<section class="cta">
  <div class="abs cta-devices" role="img" aria-label="Monitor, laptop and tablet"></div>
  <p class="abs cta-text">Our company prides itself in keeping the prices low for whatever it</p>
  <div class="abs cta-btn">Click here</div>
</section>

<section class="services">
  <h2 class="abs center section-title">Individual SEO services</h2>
  <p class="abs center services-sub">The most effective way to skyrocket your site on Searchly SERPs is to build a<br>variety of high quality backlinks to your website. Our handpicked team of link builders are SEO</p>
  <svg class="abs arrow" style="left:92px;top:238px" viewBox="0 0 40 70"><polyline points="34,2 4,35 34,68" fill="none" stroke="#8b9bb0" stroke-width="2.5"/></svg>
  <svg class="abs arrow" style="left:1066px;top:238px" viewBox="0 0 40 70"><polyline points="6,2 36,35 6,68" fill="none" stroke="#8b9bb0" stroke-width="2.5"/></svg>

  <div class="abs service" style="left:180px">
    <svg class="service-icon" viewBox="0 0 172 172" fill="none" stroke="#fff" stroke-width="5">
      <circle cx="86" cy="86" r="82"/>
      <rect x="74" y="42" width="24" height="22" fill="#fff" stroke="none"/>
      <path d="M86 64v14M52 78h68M52 78v14M120 78v14M86 78v14" stroke-width="4"/>
      <rect x="40" y="94" width="24" height="22" fill="#fff" stroke="none"/>
      <rect x="74" y="94" width="24" height="22" fill="#fff" stroke="none"/>
      <rect x="108" y="94" width="24" height="22" fill="#fff" stroke="none"/>
    </svg>
    <div class="service-label">Branding</div>
    <p class="service-text">Our company prides itself<br>in keeping the prices low<br>for whatever it takes. You</p>
  </div>
  <div class="abs service" style="left:460px">
    <svg class="service-icon" viewBox="0 0 172 172" fill="none" stroke="#fff" stroke-width="5">
      <circle cx="86" cy="86" r="82"/>
      <rect x="40" y="48" width="92" height="62" rx="4"/>
      <path d="M74 110l-6 16h36l-6-16M62 128h48"/>
      <polyline points="52,96 70,78 84,88 104,66 120,72" stroke-width="4"/>
    </svg>
    <div class="service-label">Design</div>
    <p class="service-text">Our company prides itself<br>in keeping the prices low<br>for whatever it takes. You</p>
  </div>
  <div class="abs service" style="left:738px">
    <svg class="service-icon" viewBox="0 0 172 172" fill="none" stroke="#fff" stroke-width="5">
      <circle cx="86" cy="86" r="82"/>
      <rect x="56" y="38" width="50" height="94" rx="8"/>
      <path d="M74 122h14"/>
      <circle cx="104" cy="84" r="14" fill="#30506f"/>
      <path d="M104 62v8M104 98v8M82 84h8M118 84h8M88 68l6 6M114 94l6 6M120 68l-6 6M94 94l-6 6" stroke-width="6"/>
      <circle cx="104" cy="84" r="5" fill="#fff" stroke="none"/>
    </svg>
    <div class="service-label">Development</div>
    <p class="service-text">Our company prides itself<br>in keeping the prices low<br>for whatever it takes. You</p>
  </div>
</section>

<section class="contact">
  <h2 class="abs center section-title">Get in touch</h2>
  <div class="abs field" style="left:197px;top:99px;width:386px;height:52px">Your Name</div>
  <div class="abs field" style="left:619px;top:99px;width:384px;height:52px">Your Email</div>
  <div class="abs field" style="left:197px;top:162px;width:806px;height:186px">Your Message</div>
  <div class="abs contact-btn">Sent</div>
  <nav class="abs center social-links"><span>Friendwall</span><span>Chirper</span><span>Circlenet</span><span>Workgrid</span></nav>
</section>

<footer class="site-footer">
  <div class="abs center footer-brand"><span class="brand-mark"></span><span class="brand-name">RankLoft</span></div>
  <div class="abs center footer-tag">LET US BOOST YOUR RANKINGS</div>
  <p class="abs center footer-text">The most effective way to skyrocket your site on Searchly SERPs is to build a<br>variety of high quality backlinks to your website. Our handpicked team of link builders are SEO</p>
  <div class="abs center footer-social"><span></span><span></span><span></span><span></span><span></span><span></span></div>
  <p class="abs center copyright">© 2013 Pentaly. All Rights Reserved - Terms and Conditions - Privacy Policy</p>
</footer>

</body>
</html>
```